Book Cover (Front and Rear) for E book called Quiet Mazes

Create book cover front and rear book cover for e book called quiet mazes. Quiet Mazes is a book of 99 puzzles made up of Sudoku, word scrambles, word searches, cross words, mine finder.

Looking for a fairly simple cover similar to the attached 2 designs. Must mention title of book (quiet mazes) as well as making it clear that it is a book of puzzles and my name as the author (Hollis Varga). Rear cover basically same colour as front however just plain.

```html
<!DOCTYPE html>
<html lang="en">
<head>
<meta charset="utf-8">
<title>Quiet Mazes – Cover Spread</title>
<link rel="stylesheet" href="https://fonts.googleapis.com/css2?family=Antonio:wght@700&family=Fira+Sans+Extra+Condensed:ital,wght@1,600&display=swap">
<style>
  :root {
    --stage: #3d3d3d;
    --cover-blue: #0066cc;
    --title-white: #ffffff;
    --subtitle-yellow: #f2f23a;
    --art-cyan: #00f0f5;
    --art-cyan-soft: #29d4ee;
    --band-white: #ffffff;
  }
  * { margin: 0; padding: 0; box-sizing: border-box; }
  html, body {
    width: 684px;
    height: 1200px;
    overflow: hidden;
    background: var(--stage);
  }
  .spread {
    position: absolute;
    left: 32px;
    top: 352px;
    width: 620px;
    height: 495px;
    background: var(--cover-blue);
    box-shadow: 0 14px 40px rgba(0, 0, 0, 0.55);
    overflow: hidden;
  }
  .title {
    position: absolute;
    font-family: "Antonio", "Oswald", sans-serif;
    font-weight: 700;
    color: var(--title-white);
    white-space: nowrap;
    line-height: 1;
    text-transform: uppercase;
  }
  .front-title {
    left: 465px;
    transform: translateX(-50%);
    top: 42px;
    font-size: 60px;
    letter-spacing: -0.5px;
    text-shadow: 2px 4px 6px rgba(0, 0, 0, 0.45);
  }
  .back-title {
    left: 154px;
    transform: translateX(-50%);
    top: 241px;
    font-size: 27px;
    letter-spacing: -0.3px;
  }
  .rule {
    position: absolute;
    left: 369px;
    width: 193px;
    height: 2px;
    background: var(--title-white);
  }
  .rule-top { top: 130px; }
  .rule-bottom { top: 210px; }
  .subtitle {
    position: absolute;
    left: 339px;
    width: 253px;
    top: 139px;
    font-family: "Fira Sans Extra Condensed", sans-serif;
    font-style: italic;
    font-weight: 600;
    font-size: 15.5px;
    line-height: 22.5px;
    color: var(--subtitle-yellow);
    text-align: center;
    text-transform: uppercase;
    white-space: nowrap;
  }
  .cover-art {
    position: absolute;
    background: linear-gradient(160deg, var(--art-cyan), var(--art-cyan-soft));
  }
  .front-art { left: 398px; top: 240px; width: 133px; height: 132px; }
  .back-art { left: 127px; top: 274px; width: 45px; height: 45px; }
  .author-band {
    position: absolute;
    left: 311px;
    top: 432px;
    width: 309px;
    height: 55px;
    background: var(--band-white);
    display: flex;
    align-items: center;
    justify-content: center;
  }
  .author {
    font-family: "Antonio", "Oswald", sans-serif;
    font-weight: 700;
    font-size: 37px;
    line-height: 1;
    color: var(--cover-blue);
    text-transform: uppercase;
    white-space: nowrap;
  }
</style>
</head>
<body>
  <main class="spread">
    <section class="back-cover">
      <h2 class="title back-title">Quiet Mazes</h2>
      <div class="cover-art back-art" role="img" aria-label="Small cyan crossword-grid emblem"></div>
    </section>

    <section class="front-cover">
      <h1 class="title front-title">Quiet Mazes</h1>
      <div class="rule rule-top"></div>
      <p class="subtitle">Sudoku , Word Scrambles,<br>Word Searches,<br>Cross Words, Mine Finder</p>
      <div class="rule rule-bottom"></div>
      <div class="cover-art front-art" role="img" aria-label="Cyan crossword-grid illustration"></div>
      <div class="author-band">
        <p class="author">Hollis Varga</p>
      </div>
    </section>
  </main>
</body>
</html>
```